4 sided DL flyer for a high end jewellery brand

I need a 4 sided DL flyer (21cm X 10cm) from my jewellery brand, ELUNE. My brand is UPSCALE and the flyer should be ELEGANT. I am uploading some sample images that can be used to create the flyer; however, I will get the final images in few days time. I am also attaching the following (1) My logo files - has the words ELUNE and icon (2) my business card - the front has the marble background that I am looking to use for the flyer and the logo style (gold foil). The back has the business details (3) mood board - blush pink/copper can also be used. Also please have space to write few lines about the brand and jewellery within the flyer. The flyer should be landscape.
Look and feel

```html
<!DOCTYPE html>
<html lang="en">
<head>
<meta charset="utf-8">
<title>ELUNE – Jewellery Collections</title>
<link rel="stylesheet" href="https://fonts.googleapis.com/css2?family=Cinzel:wght@400;500&family=Open+Sans:wght@400;600&display=swap">
<style>
  :root {
    --blush: #e8958c;
    --blush-line: #eea69e;
    --ink: #1e1e1e;
    --paper: #ffffff;
    --silver-a: #f2f2f2;
    --silver-b: #c9c9c9;
    --gold-a: #f3e7b0;
    --gold-b: #c9b45a;
    --marble-a: #f4f1ef;
    --marble-b: #d9d2cf;
    --box-a: #3a3a3a;
    --box-b: #111111;
  }
  * { margin: 0; padding: 0; box-sizing: border-box; }
  html, body { width: 1132px; height: 1200px; overflow: hidden; background: var(--paper); }
  .flyer {
    position: relative; width: 1132px; height: 1200px; background: var(--paper);
    font-family: "Open Sans", Arial, sans-serif; color: var(--ink);
  }
  .edge { position: absolute; top: 0; width: 10px; height: 1200px; background: var(--blush-line); }
  .edge--left { left: 0; }
  .edge--right { right: 0; }

  .heading {
    font-family: "Cinzel", "Times New Roman", serif; color: var(--blush);
    font-weight: 400; letter-spacing: 0.5px; white-space: nowrap;
  }

  /* Collections column */
  .collection { position: absolute; left: 0; width: 566px; height: 161px; }
  .collection__image { position: absolute; left: 62px; top: 0; width: 138px; height: 136px; border-radius: 50%; }
  .collection__image--silver { background: radial-gradient(circle, var(--silver-a), var(--silver-b) 70%, transparent 72%); }
  .collection__image--gold { background: radial-gradient(circle, var(--gold-a), var(--gold-b) 68%, transparent 70%); }
  .collection__title { position: absolute; left: 230px; top: 40px; font-size: 21px; }
  .collection__text { position: absolute; left: 230px; top: 66px; font-size: 18px; line-height: 24px; width: 300px; }
  .collection__price { position: absolute; left: 230px; top: 146px; font-size: 14.5px; font-weight: 600; color: var(--blush); white-space: nowrap; }

  .lifestyle-photo {
    position: absolute; left: 10px; top: 1018px; width: 556px; height: 182px;
    background: linear-gradient(135deg, var(--marble-a), var(--marble-b) 55%, #c9a89a);
  }

  /* Featured column */
  .feature-title { position: absolute; left: 600px; width: 500px; top: 42px; text-align: center; font-size: 25px; }
  .divider { position: absolute; left: 620px; top: 84px; width: 458px; height: 28px; }

  .feature { position: absolute; left: 620px; width: 480px; height: 268px; }
  .feature__image { position: absolute; left: 10px; width: 170px; height: 170px; border-radius: 50%;
    background: radial-gradient(circle, var(--silver-a), var(--silver-b) 65%, transparent 68%); }
  .feature__title { position: absolute; left: 226px; top: 0; font-size: 21px; }
  .feature__price { position: absolute; left: 226px; top: 27px; font-size: 14.5px; font-weight: 600; color: var(--blush); }
  .feature__specs { position: absolute; left: 226px; top: 56px; list-style: none; font-size: 18px; line-height: 24px; }
  .feature__specs li { white-space: nowrap; }
  .feature__specs li::before { content: "•"; color: var(--blush); margin-right: 4px; }

  .giftbox-photo {
    position: absolute; left: 628px; top: 956px; width: 420px; height: 160px;
    background: linear-gradient(180deg, var(--box-a), var(--box-b) 80%, #ffffff 100%);
    border-radius: 2px;
  }
  .giftbox-note {
    position: absolute; left: 600px; width: 500px; top: 1150px; text-align: center;
    font-size: 16.5px; font-weight: 600; color: var(--blush); white-space: nowrap;
  }
</style>
</head>
<body>
<main class="flyer">
  <div class="edge edge--left"></div>
  <div class="edge edge--right"></div>

  <section class="collections">
    <article class="collection" style="top:20px">
      <div class="collection__image collection__image--silver" role="img" aria-label="Flower pendant necklace with crystals"></div>
      <h2 class="heading collection__title">Necklace Collection</h2>
      <p class="collection__text">Brief Description Here...is es sitibus iderum senis ipsandest expelenisen ia ius et ullenim siminciis autatur</p>
      <p class="collection__price">Prices start from just $40 incl. GST</p>
    </article>
    <article class="collection" style="top:181px">
      <div class="collection__image collection__image--silver" role="img" aria-label="Open silver cuff bracelet with triangle and bar ends"></div>
      <h2 class="heading collection__title">Bracelet Collection</h2>
      <p class="collection__text">Brief Description Here...is es sitibus iderum senis ipsandest expelenisen ia ius et ullenim siminciis autatur</p>
      <p class="collection__price">Prices start from just $40 incl. GST</p>
    </article>
    <article class="collection" style="top:342px">
      <div class="collection__image collection__image--silver" role="img" aria-label="Pair of heart stud earrings with crystals"></div>
      <h2 class="heading collection__title">Earring Collection</h2>
      <p class="collection__text">Brief Description Here...is es sitibus iderum senis ipsandest expelenisen ia ius et ullenim siminciis autatur</p>
      <p class="collection__price">Prices start from just $40 incl. GST</p>
    </article>
    <article class="collection" style="top:503px">
      <div class="collection__image collection__image--gold" role="img" aria-label="Gold crossover ring with crystals"></div>
      <h2 class="heading collection__title">Ring Collection</h2>
      <p class="collection__text">Brief Description Here...is es sitibus iderum senis ipsandest expelenisen ia ius et ullenim siminciis autatur</p>
      <p class="collection__price">Prices start from just $40 incl. GST</p>
    </article>
    <article class="collection" style="top:664px">
      <div class="collection__image collection__image--gold" role="img" aria-label="Round gold filigree pendant"></div>
      <h2 class="heading collection__title">Pendant Collection</h2>
      <p class="collection__text">Brief Description Here...is es sitibus iderum senis ipsandest expelenisen ia ius et ullenim siminciis autatur</p>
      <p class="collection__price">Prices start from just $20 incl. GST</p>
    </article>
    <article class="collection" style="top:825px">
      <div class="collection__image collection__image--silver" role="img" aria-label="Fine silver anklet chain with charms"></div>
      <h2 class="heading collection__title">Anklet Collection</h2>
      <p class="collection__text">Brief Description Here...is es sitibus iderum senis ipsandest expelenisen ia ius et ullenim siminciis autatur</p>
      <p class="collection__price">Prices start from just $30 incl. GST</p>
    </article>
  </section>

  <div class="lifestyle-photo" role="img" aria-label="Stacked rose and silver rings with a pearl on white marble"></div>

  <section class="featured">
    <h1 class="heading feature-title">Give the gift of endless beauty</h1>
    <svg class="divider" viewBox="0 0 458 28" aria-hidden="true">
      <line x1="0" y1="14" x2="200" y2="14" stroke="#eea69e" stroke-width="1"/>
      <line x1="258" y1="14" x2="458" y2="14" stroke="#eea69e" stroke-width="1"/>
      <path d="M229 2 L241 16 L229 24 L217 16 Z M229 2 L229 24 M217 16 L241 16" fill="none" stroke="#e8958c" stroke-width="1.4"/>
    </svg>

    <article class="feature" style="top:190px">
      <div class="feature__image" style="top:-40px;height:210px" role="img" aria-label="Flower pendant necklace on fine chain"></div>
      <h2 class="heading feature__title">Featured Item</h2>
      <p class="feature__price">$40.00 incl. GST</p>
      <ul class="feature__specs">
        <li>925 sterling silver</li>
        <li>Heart with CZ: 9mm X 9mm</li>
        <li>Chain: 40.5cm</li>
        <li>Complimentary gift box</li>
      </ul>
    </article>

    <article class="feature" style="top:458px">
      <div class="feature__image" style="top:20px;height:110px" role="img" aria-label="Pair of heart stud earrings with crystals"></div>
      <h2 class="heading feature__title">Featured Item</h2>
      <p class="feature__price">$40.00 incl. GST</p>
      <ul class="feature__specs">
        <li>925 sterling silver</li>
        <li>Heart with CZ: 9mm X 9mm</li>
        <li>Chain: 40.5cm</li>
        <li>Complimentary gift box</li>
      </ul>
    </article>

    <article class="feature" style="top:726px">
      <div class="feature__image" style="top:-10px;height:160px" role="img" aria-label="Open silver cuff bracelet with triangle and bar ends"></div>
      <h2 class="heading feature__title">Featured Item</h2>
      <p class="feature__price">$40.00 incl. GST</p>
      <ul class="feature__specs">
        <li>925 sterling silver</li>
        <li>Heart with CZ: 9mm X 9mm</li>
        <li>Chain: 40.5cm</li>
        <li>Complimentary gift box</li>
      </ul>
    </article>

    <div class="giftbox-photo" role="img" aria-label="Black ELUNE gift boxes in three sizes"></div>
    <p class="giftbox-note">All of our jewellery comes with a complimentary gift box</p>
  </section>
</main>
</body>
</html>
```